Company identity deisgn should support 2 languages

I would like to get our company identity design
This includes the following only
Business Cards 2 languages Arabic and English
Email signature
Letterhead
Linkedin profile images
Attached is the logo in Ai format

Requirements
Must have
• For business card
Must have
Name and Adrees in arabic
Name and Address in english
You might use both side of the card
Should not have
• Any pictures other than the logo

```html
<!DOCTYPE html>
<html lang="en">
<head>
<meta charset="utf-8">
<title>Nexora Systems – Stationery</title>
<link href="https://fonts.googleapis.com/css2?family=Lato:wght@400;700&family=Tajawal:wght@400;500&display=swap" rel="stylesheet">
<style>
:root{
  --blue:#1f73bf;
  --blue-dark:#1862a6;
  --orange:#ec8a52;
  --ink:#2c2c2c;
  --grey:#6d6d6d;
  --band-grey:#c9cccf;
  --paper:#ffffff;
  --backdrop:#e3e6e7;
}
*{box-sizing:border-box;margin:0;padding:0}
html,body{width:1200px;height:1020px;overflow:hidden}
body{background:var(--backdrop);font-family:"Lato","Tajawal",sans-serif;color:var(--ink);position:relative}
.ar{font-family:"Tajawal",sans-serif;direction:rtl}

/* brand lockup */
.brand{display:flex;align-items:center;gap:7px;color:var(--blue);font-weight:700;letter-spacing:.06em;white-space:nowrap}
.brand .dot{width:1em;height:1em;border-radius:50%;background:var(--blue);flex:none}
.brand.light{color:#fff}
.brand.light .dot{background:#fff}

/* letterhead */
.letterhead{position:absolute;left:40px;top:120px;width:600px;height:777px;background:var(--paper);box-shadow:0 6px 18px rgba(0,0,0,.12)}
.letterhead .brand{position:absolute;left:40px;top:42px;font-size:15px}
.lh-address{position:absolute;right:38px;top:38px;display:flex;gap:10px;font-size:9.5px;line-height:1.2}
.lh-address .ar{text-align:right;font-size:8.5px;line-height:1.35;padding-right:10px;border-right:1px solid var(--grey)}
.letter{position:absolute;left:64px;top:170px;width:470px;font-size:9.4px;line-height:1.38;color:#555}
.letter p{margin-bottom:13px;text-align:justify}
.letter .date{margin-bottom:15px}
.letter .recipient{margin-bottom:20px}
.letter .recipient strong{color:var(--ink)}
.signature-area{display:block;width:190px;height:26px;margin-top:4px;background:linear-gradient(90deg,#ececec,#f7f7f7);border-radius:3px}
.lh-footer{position:absolute;left:0;right:0;bottom:10px;height:22px;background:var(--blue);color:#fff;font-size:9.5px;display:flex;justify-content:center;align-items:center;gap:16px}
.contact{display:inline-flex;align-items:center;gap:4px}
.contact svg{width:.95em;height:.95em}

/* email signature */
.email-sig{position:absolute;left:680px;top:120px;width:480px;height:120px;background:var(--paper);border-radius:10px;overflow:hidden;box-shadow:0 6px 16px rgba(0,0,0,.12)}
.email-sig svg.shape{position:absolute;inset:0}
.email-sig .brand{position:absolute;left:20px;top:24px;font-size:11px}
.email-sig .rule{position:absolute;left:19px;top:55px;width:17px;height:2px;background:var(--orange)}
.email-sig .tagline{position:absolute;left:19px;top:61px;font-size:8px;line-height:1.25;width:170px}
.es-address{position:absolute;left:254px;top:24px;display:flex;gap:8px;color:#fff;font-size:8px;line-height:1.2}
.es-address .ar{font-size:6.8px;line-height:1.35;padding-right:8px;border-right:1px solid #fff}
.es-contacts{position:absolute;right:26px;bottom:10px;display:flex;gap:10px;font-size:8.2px}
.es-contacts svg{color:var(--blue)}

/* business cards */
.card{position:absolute;left:720px;width:400px;height:227px;border-radius:12px;overflow:hidden;box-shadow:0 6px 16px rgba(0,0,0,.14)}
.card-front{top:280px;background:var(--paper)}
.card-front .band{position:absolute;left:24px;top:0;bottom:0;width:44px;background:var(--blue)}
.card-front .band::before{content:"";position:absolute;left:0;right:0;top:0;height:48px;background:var(--band-grey)}
.card-front .brand{position:absolute;left:80px;top:32px;font-size:10px}
.card-front .person-ar{position:absolute;left:88px;top:100px;text-align:right;font-size:8px;line-height:1.3}
.person-ar .name{color:var(--blue);font-size:10px;font-weight:500}
.person-ar .rule{display:block;width:24px;height:2px;background:var(--grey);margin:8px 0 8px auto}
.card-front .person-en{position:absolute;left:228px;top:98px;font-size:7.4px;line-height:1.35}
.person-en .name{color:var(--blue);font-size:12px;font-weight:700}
.person-en .rule{display:block;width:24px;height:2px;background:var(--blue);margin:8px 0 8px}
.card-front .contacts{position:absolute;left:88px;bottom:18px;display:flex;gap:9px;font-size:7.4px}
.card-front .contacts svg{color:var(--blue)}
.card-back{top:530px;background:var(--blue);display:flex;flex-direction:column;align-items:center;justify-content:center}
.card-back .brand{font-size:15px;margin-top:14px}
.card-back .web{position:absolute;bottom:34px;color:#dbe8f5;font-size:8px;letter-spacing:.08em}
</style>
</head>
<body>

<svg width="0" height="0" style="position:absolute">
  <symbol id="i-phone" viewBox="0 0 16 16"><path d="M4 1.5l2.2 2.8-1.3 1.7a9 9 0 0 0 5.1 5.1l1.7-1.3 2.8 2.2-1.4 2.4C7.5 14.2 1.8 8.5 1.6 2.9z" fill="currentColor"/></symbol>
  <symbol id="i-mail" viewBox="0 0 16 16"><rect x="1" y="3" width="14" height="10" rx="1" fill="currentColor"/><path d="M1.5 3.8L8 9l6.5-5.2" stroke="#fff" stroke-width="1.2" fill="none"/></symbol>
  <symbol id="i-web" viewBox="0 0 16 16"><g fill="none" stroke="currentColor" stroke-width="1.4"><circle cx="8" cy="8" r="6.3"/><ellipse cx="8" cy="8" rx="2.7" ry="6.3"/><path d="M1.8 8h12.4"/></g></symbol>
</svg>

<!-- Letterhead -->
<section class="letterhead">
  <div class="brand"><span class="dot"></span>NEXORA SYSTEMS</div>
  <div class="lh-address">
    <div class="ar">برج الساحل الدور 12<br>طريق الخليج<br>الكورنيش الدمام 31411</div>
    <div>Sahel Tower, 12th floor<br>Gulf Road<br>Corniche District, Dammam 31411</div>
  </div>
  <div class="letter">
    <div class="date">01 January 2050</div>
    <div class="recipient"><strong>Company (Pvt) Ltd.</strong><br>PO Box 3355 Mainville St<br>Sample City Country 3355</div>
    <p>Dear Daniel Hawthorne,</p>
    <p>Lorem ipsum dolor sit amet, consectetuer adipiscing elit, sed diam nonummy nibh euismod tincidunt ut laoreet dolore magna aliquam erat volutpat. Ut wisi enim ad minim veniam, quis nostrud exerci tation ullamcorper suscipit lobortis nisl ut aliquip ex ea commodo consequat. Duis dolore te feugait nulla facilisi. Nam liber tempor cum soluta nobis eleifend option congue nihil imperdiet doming id quod mazim placerat facer possim assum. Lorem ipsum dolor sit amet, consectetuer adipiscing elit, sed diam nonummy nibh euismod tincidunt ut laoreet dolore magna aliquam erat volutpat. Ut wisi enim ad minim veniam, quis nostrud exerci tation ullamcorper suscipit lobortis nisl ut aliquip ex ea commodo consequat.</p>
    <p>Consectetuer adipiscing elit, sed diam nonummy nibh euismod tincidunt ut laoreet dolore magna aliquam erat volutpat. Ut wisi enim ad minim veniam, quis nostrud exerci tation ullamcorper suscipit lobortis nisl ut aliquip ex ea commodo consequat. Consectetuer adipiscing elit, sed diam nonummy nibh euismod tincidunt ut laoreet dolore magna aliquam erat volutpat. Ut wisi enim ad minim veniam, quis nostrud exerci tation ullamcorper suscipit lobortis nisl ut aliquip ex ea commodo consequat.</p>
    <p>Consectetuer adipiscing elit, sed diam nonummy nibh euismod tincidunt ut laoreet dolore magna aliquam erat volutpat. Ut wisi enim ad minim veniam, quis nostrud exerci tation ullamcorper suscipit lobortis nisl ut aliquip ex ea commodo consequat. Consectetuer adipiscing elit, sed diam nonummy nibh euismod tincidunt ut laoreet dolore magna aliquam erat volutpat. Ut wisi enim ad minim veniam, quis nostrud exerci tation ullamcorper suscipit lobortis nisl ut aliquip ex ea commodo consequat.</p>
    <p style="margin-top:30px;margin-bottom:0">Sincerely Yours</p>
    <span class="signature-area" role="img" aria-label="Handwritten signature of the sender"></span>
  </div>
  <footer class="lh-footer">
    <span class="contact"><svg><use href="#i-phone"/></svg>+966 1100 555 000</span>
    <span class="contact"><svg><use href="#i-mail"/></svg>info@nexorasys.com</span>
    <span class="contact"><svg><use href="#i-web"/></svg>www.nexorasys.com</span>
  </footer>
</section>

<!-- Email signature -->
<section class="email-sig">
  <svg class="shape" viewBox="0 0 480 120" preserveAspectRatio="none">
    <polygon points="207,0 480,0 480,54 246,96" fill="var(--orange)"/>
    <polygon points="212,0 480,0 480,44 246,94 226,60" fill="var(--blue)"/>
    <polygon points="300,82 480,46 480,56" fill="var(--orange)"/>
  </svg>
  <div class="brand"><span class="dot"></span>NEXORA SYSTEMS</div>
  <div class="rule"></div>
  <div class="tagline">Smart products and solutions have already touched our lives.</div>
  <div class="es-address">
    <div class="ar">برج الساحل الدور 12<br>طريق الخليج<br>الكورنيش الدمام 31411</div>
    <div>Sahel Tower, 12th floor<br>Gulf Road<br>Corniche District, Dammam 31411</div>
  </div>
  <div class="es-contacts">
    <span class="contact"><svg><use href="#i-phone"/></svg>+966 1100 555 000</span>
    <span class="contact"><svg><use href="#i-mail"/></svg>info@nexorasys.com</span>
    <span class="contact"><svg><use href="#i-web"/></svg>www.nexorasys.com</span>
  </div>
</section>

<!-- Business card front -->
<section class="card card-front">
  <div class="band"></div>
  <div class="brand"><span class="dot"></span>NEXORA SYSTEMS</div>
  <div class="person-ar ar">
    <div class="name">خالد الحربي</div>
    <div>مدير تطوير الأعمال</div>
    <span class="rule"></span>
    <div>برج الساحل الدور 12<br>طريق الخليج<br>الكورنيش الدمام 31411</div>
  </div>
  <div class="person-en">
    <div class="name">Khalid Alharbi</div>
    <div>Business Development Director</div>
    <span class="rule"></span>
    <div>Sahel Tower, 12th floor<br>Gulf Road<br>Corniche District, Dammam 31411</div>
  </div>
  <div class="contacts">
    <span class="contact"><svg><use href="#i-phone"/></svg>+966 1100 555 000</span>
    <span class="contact"><svg><use href="#i-mail"/></svg>info@nexorasys.com</span>
    <span class="contact"><svg><use href="#i-web"/></svg>www.nexorasys.com</span>
  </div>
</section>

<!-- Business card back -->
<section class="card card-back">
  <div class="brand light"><span class="dot"></span>NEXORA SYSTEMS</div>
  <div class="web">www.nexorasys.com</div>
</section>

</body>
</html>
```